Business Card for QRB Farmstock

Custom Business Card Brief:
1. We need two designs for this single client, QRB Farmstock LLC and both designs will end up with rounded corner printed cards that fit the PRINTLY.com design format for their special printing style.
2. My client needs two separate card designs since half of their target market is for farm owners in the Cattle and Beef world. The other half of their target market is working with Equine aka Horse farm owners.
3. The look for two card designs can be similar to ensure branding consistency but we will need some space sizing differences so the cards stand out differently in regards to how the services mentioned are laid out on the front of each card design.
4. Both card designs require the front of the card holding all of the great design work. The back of these 2-sided cards will remain white and can just have the contact information listed "again" on the back to match the contact information provided on the front.
5. Card Design 1 will be for Equine customers, Card Design 2 will be for his Cattle/Beef customers.
6. Card Design 1 (Equine) we are thinking we set aside 70% of the card to be dedicated to the Services listed section while the remaining 30% of the front of the card space will hold a smaller logo image space along with his name and contact information.
7. Card Design 2 (Cattle/Beef) we will need opposite of my last point. We want 70% of the card dedicated to a larger logo space and his contact information while the remaining 30% listing the services provided.
8. Card Design #1 - Equine - his Services space should include:
- Equine Mortality Services
- General Removal
- Cremation
- Transportation for Necropsy
9. Card Design #2 - Cattle/Beef - his Services space should include: General Livestock Services, Hauling, Order Buying, Dealing, Dead Stock Removal
10. Contact Information for both card designs:
- Gerald R. Fenwick (owner)
- QRB Farmstock LLC (company)
- 555-318-4692 (phone)
- info@qrbfarmstockservices.example (email)
- QRBFarmstockServices.example (website)
11. Additional Branding Details - The color codes aka pantone colors that are in the current logo file design:
- Blue Pantone 7686C
- Grey Pantone 422C
12. The font styles used in the logo:
- Nexa Bold
- Nexa Rust Slab Black Shadow
13. Back of both card designs, just list his contact information in larger size to stand out more on the white back:
- 555-318-4692 (phone)
Updates

Okay thanks for confirming that our final design files will be ready for the PRINTLY.com format. I noticed the 2nd place vertical card already had rounded corners but the horizontal design that was in 1st place still had sharp square corners. When using the PRINTLY.com format we will be rounding all of the corners of both cards for print. So we just wanted to make sure that both sets of files will be in a rounded design meeting their format sizing to ensure no content from your great designs gets cut off. Thank you again for your attention to detail. ~ Derek

Target Market(s)

Business to Business

Industry/Entity Type

Farming, Agriculture, Livestock

Contact Information for Business Card

Clients' logo, his contact info, and his different services on two similar final card designs.

Font styles to use
Other font styles liked:
• Look at the brief to see how his logo fonts are currently.

Requirements
Must have
• Two versions of the card, one for the Equine horse market, and one for the Cattle/Beef market of farming.
Nice to have
• Clean, sharp, concise.
Should not have
• No flashy or cartoony designs.

```html
<!DOCTYPE html>
<html lang="en">
<head>
<meta charset="utf-8">
<title>QRB Farmstock Business Cards</title>
<link rel="stylesheet" href="https://fonts.googleapis.com/css2?family=Montserrat:wght@500;600;700&display=swap">
<style>
  :root {
    --brand-blue: #1f4f8f;
    --brand-grey: #9ea2a2;
    --ink: #111111;
    --paper: #ffffff;
    --page: #ffffff;
  }
  * { margin: 0; padding: 0; box-sizing: border-box; }
  html, body {
    width: 1200px; height: 901px; overflow: hidden;
    background: var(--page);
    font-family: "Montserrat", sans-serif;
  }
  .canvas { position: relative; width: 1200px; height: 901px; }
  .card {
    position: absolute; top: 115px;
    width: 439px; height: 670px;
    background: var(--paper);
    border-radius: 34px;
    overflow: hidden;
    box-shadow: 0 6px 22px rgba(0,0,0,0.28);
  }
  .card--equine { left: 120px; }
  .card--cattle { left: 641px; }
  .card__band { position: absolute; inset: 0; width: 439px; height: 670px; }
  .brand-name {
    position: absolute; left: 0; right: 0; text-align: center;
    color: var(--brand-blue); font-weight: 700; letter-spacing: 1px;
  }
  .card--equine .brand-name { top: 72px; font-size: 36px; }
  .card--cattle .brand-name { top: 102px; font-size: 44px; }
  .owner-name {
    position: absolute; left: 0; right: 0; text-align: center;
    color: var(--ink); font-weight: 600; letter-spacing: -0.3px;
  }
  .card--equine .owner-name { top: 160px; font-size: 31px; }
  .card--cattle .owner-name { top: 230px; font-size: 34px; }
  .services text { fill: var(--paper); font-family: "Montserrat", sans-serif; font-weight: 600; }
  .contact {
    position: absolute; text-align: right; list-style: none;
    color: var(--ink); font-weight: 500;
  }
  .card--equine .contact { right: 32px; top: 540px; font-size: 17px; line-height: 24.5px; }
  .card--cattle .contact { right: 30px; top: 522px; font-size: 19px; line-height: 29px; }
</style>
</head>
<body>
<main class="canvas">
  <article class="card card--equine">
    <svg class="card__band services" viewBox="0 0 439 670" aria-label="Equine services">
      <polygon points="0,305 439,196 439,484 0,592" fill="var(--brand-blue)"/>
      <text font-size="30" transform="translate(32 359) rotate(-14)">Transport for Necropsy</text>
      <text font-size="30" transform="translate(46 413) rotate(-14)">Equine Mortality</text>
      <text font-size="30" transform="translate(60 464) rotate(-14)">General Removal</text>
      <text font-size="30" transform="translate(73 514) rotate(-14)">Cremation</text>
    </svg>
    <div class="brand-name">QRB Farmstock</div>
    <h2 class="owner-name">Gerald R. Fenwick</h2>
    <ul class="contact">
      <li>QRB Farmstock LLC</li>
      <li>555-318-4692</li>
      <li>info@qrbfarmstockservices.example</li>
      <li>QRBFarmstockServices.example</li>
    </ul>
  </article>

  <article class="card card--cattle">
    <svg class="card__band services" viewBox="0 0 439 670" aria-label="Cattle and beef services">
      <polygon points="0,382 439,277 439,463 0,568" fill="var(--brand-blue)"/>
      <text font-size="21" transform="translate(60 399) rotate(-14)">General Livestock Services</text>
      <text font-size="21" transform="translate(66 430) rotate(-14)">Hauling</text>
      <text font-size="21" transform="translate(73 460) rotate(-14)">Order Buying</text>
      <text font-size="21" transform="translate(80 490) rotate(-14)">Dealing</text>
      <text font-size="21" transform="translate(87 521) rotate(-14)">Dead Stock Removal</text>
    </svg>
    <div class="brand-name">QRB Farmstock</div>
    <h2 class="owner-name">Gerald R. Fenwick</h2>
    <ul class="contact">
      <li>QRB Farmstock LLC</li>
      <li>555-318-4692</li>
      <li>info@qrbfarmstockservices.example</li>
      <li>QRBFarmstockServices.example</li>
    </ul>
  </article>
</main>
</body>
</html>
```